Belvoro Website

I need a website for a startup company that provides GIS (Geographic Information Services) staffing and products for local cities. Current website is www.belvorogroup.com

```html
<!DOCTYPE html>
<html lang="en">
<head>
<meta charset="utf-8">
<title>Belvoro Group</title>
<link href="https://fonts.googleapis.com/css2?family=Gelasio:wght@400;500&family=Poppins:wght@400;500&display=swap" rel="stylesheet">
<style>
:root{
  --navy:#1c1c2c;
  --navy-deep:#161624;
  --accent:#2ba3cc;
  --white:#ffffff;
  --ink:#1d1d26;
  --card:#f3f3f4;
  --muted:#3a3a44;
}
*{box-sizing:border-box;margin:0;padding:0}
html,body{width:1200px;height:3146px;overflow:hidden}
body{background:var(--navy);font-family:"Poppins",sans-serif;color:var(--ink);position:relative}
.abs{position:absolute}
.logo{font-family:"Gelasio",serif;font-weight:400;font-size:46px;letter-spacing:.2px}
.btn{position:absolute;display:flex;align-items:center;justify-content:center;border-radius:20px;font-size:17px;font-weight:400;white-space:nowrap}
.btn-accent{background:var(--accent);color:var(--white)}
.btn-outline{border:1.5px solid var(--white);color:var(--white)}
.btn-light{background:var(--white);color:var(--ink)}

/* header & hero */
.hero{position:absolute;left:0;top:0;width:1200px;height:670px;background:var(--navy-deep)}
.hero-visual{position:absolute;left:430px;top:95px;width:770px;height:575px;
  background:radial-gradient(ellipse at 55% 45%,#1f5a4c 0%,#1a3338 35%,#181c2a 70%,var(--navy-deep) 100%)}
.header-band{position:absolute;left:0;top:0;width:1200px;height:95px;background:var(--navy)}
.site-logo{left:88px;top:28px;color:var(--white)}
.nav a{position:absolute;top:54px;color:var(--white);font-size:17px;text-decoration:none}
.headline{left:88px;color:var(--white);font-weight:400;line-height:1}
.headline .hl{color:var(--accent)}

/* main white section */
.sheet{position:absolute;left:0;top:685px;width:1200px;height:1510px;background:var(--white);border-radius:100px}
.section-title{font-size:46px;font-weight:400;color:var(--ink)}
.body-text{font-size:18px;line-height:31px;color:var(--muted)}
.card{position:absolute;background:var(--card);border-radius:16px;overflow:hidden}
.card-title{position:absolute;font-size:40px;line-height:46px;font-weight:400;color:var(--ink)}
.card-text{position:absolute;color:var(--muted)}
.photo{position:absolute}

/* contact */
.contact-title{color:var(--white)}
.field{position:absolute;border:1.5px solid var(--white);border-radius:24px;color:var(--white);font-size:17px;padding-left:17px;display:flex;align-items:center}
.field-message{align-items:flex-start;padding-top:14px}

/* footer */
.footer{position:absolute;left:0;top:2865px;width:1200px;height:281px;background:var(--white);border-radius:90px 90px 0 0}
.footer-nav a{position:absolute;top:80px;font-size:17px;color:var(--ink);text-decoration:none}
.social{position:absolute;top:170px;width:20px;height:20px;border-radius:50%;background:var(--ink)}
</style>
</head>
<body>

<section class="hero">
  <div class="hero-visual" role="img" aria-label="Glowing green 3D terrain point cloud with a map pin above a smartphone"></div>
  <div class="header-band"></div>
  <div class="abs logo site-logo">Belvoro Group</div>
  <nav class="nav">
    <a style="left:653px">Home</a>
    <a style="left:748px">About Us</a>
    <a style="left:864px">Services
      <svg width="10" height="7" viewBox="0 0 10 7" style="margin-left:4px;vertical-align:middle"><path d="M1 1l4 4 4-4" fill="none" stroke="#fff" stroke-width="1.3"/></svg></a>
  </nav>
  <div class="btn btn-accent" style="left:988px;top:48px;width:125px;height:35px">Contact Us</div>

  <div class="abs headline" style="top:198px;font-size:62px">WE MAKE</div>
  <div class="abs headline hl" style="top:266px;font-size:76px;color:var(--accent)">GIS WORK</div>
  <div class="abs headline" style="top:358px;font-size:62px">FOR YOU</div>
  <div class="btn btn-accent" style="left:85px;top:468px;width:126px;height:34px">Contact Us</div>
  <div class="btn btn-outline" style="left:230px;top:468px;width:168px;height:34px">Services Details</div>
</section>

<main class="sheet">
  <h2 class="abs section-title" style="left:0;width:1200px;text-align:center;top:82px">About us</h2>
  <p class="abs body-text" style="left:150px;width:900px;text-align:center;top:164px">We are an innovative team of geospatial experts with <strong style="color:var(--ink);font-weight:500">25 years of experience in the field of GIS.</strong> We specialize in providing results-driven GIS solutions for local government and the private sector.</p>
  <div class="btn btn-accent" style="left:534px;top:256px;width:125px;height:34px">Read More</div>

  <h2 class="abs section-title" style="left:90px;top:364px">Our services</h2>
  <p class="abs body-text" style="left:623px;width:490px;top:370px">Lorem ipsum dolor sit amet consectetur adipiscing elit sed do eiusmod tempor incididunt ut labore et dolore magna aliqua.</p>

  <article class="card" style="left:88px;top:529px;width:1026px;height:372px">
    <h3 class="card-title" style="left:46px;top:30px">GIS<br>Consulting</h3>
    <p class="card-text body-text" style="left:46px;top:148px;width:310px">Lorem ipsum dolor sit am et consectetur adipiscing elit sed do eiusmod tempor incididunt ut labore et dolore magna aliqua.</p>
    <div class="btn btn-accent" style="left:46px;top:299px;width:136px;height:33px">Learn More</div>
    <div class="photo" style="left:402px;top:0;width:624px;height:372px;background:linear-gradient(120deg,#e6e8ee 0%,#c9ccd8 45%,#3e5494 80%,#2c3f7c 100%)" role="img" aria-label="Hand holding a phone showing a city parcel map over topographic contour lines"></div>
  </article>

  <article class="card" style="left:88px;top:923px;width:499px;height:480px">
    <div class="photo" style="left:0;top:0;width:499px;height:239px;background:linear-gradient(180deg,#6f8fb5 0%,#3d5877 60%,#263245 100%)" role="img" aria-label="Hand holding a phone with location markers over a city skyline"></div>
    <h3 class="card-title" style="left:46px;top:262px">GIS Applications</h3>
    <p class="card-text" style="left:46px;top:328px;width:420px;font-size:13.5px;line-height:22px">Lorem ipsum dolor sit am et consectetur adipiscing elit sed do eiusmod tempor incididunt ut labore et dolore magna aliqua.</p>
    <div class="btn btn-accent" style="left:46px;top:402px;width:136px;height:34px">Learn More</div>
  </article>

  <article class="card" style="left:613px;top:923px;width:499px;height:480px">
    <div class="photo" style="left:0;top:0;width:499px;height:238px;background:linear-gradient(135deg,#1a2f9e 0%,#3b46c9 45%,#7a3fd0 75%,#0d1038 100%)" role="img" aria-label="Glowing network cable over a digital world map"></div>
    <h3 class="card-title" style="left:44px;top:262px">Spatial Data Solutions</h3>
    <p class="card-text" style="left:44px;top:328px;width:420px;font-size:13.5px;line-height:22px">Lorem ipsum dolor sit am et consectetur adipiscing elit sed do eiusmod tempor incididunt ut labore et dolore magna aliqua.</p>
    <div class="btn btn-accent" style="left:44px;top:402px;width:136px;height:34px">Learn More</div>
  </article>
</main>

<section>
  <h2 class="abs section-title contact-title" style="left:0;width:1200px;text-align:center;top:2264px">Get in touch</h2>
  <p class="abs body-text" style="left:190px;width:820px;text-align:center;top:2338px;color:var(--white)">Lorem ipsum dolor sit amet consectetur adipiscing elit sed do eiusmod tempor incididunt ut labore et dolore magna aliqua.</p>
  <div class="field" style="left:94px;top:2451px;width:243px;height:48px">First Name*</div>
  <div class="field" style="left:351px;top:2451px;width:244px;height:48px">Last Name*</div>
  <div class="field" style="left:608px;top:2451px;width:243px;height:48px">Email*</div>
  <div class="field" style="left:866px;top:2451px;width:244px;height:48px">Phone no.*</div>
  <div class="field field-message" style="left:94px;top:2522px;width:1016px;height:188px">Message*</div>
  <div class="btn btn-light" style="left:526px;top:2731px;width:149px;height:34px">Send</div>
</section>

<footer class="footer">
  <div class="abs logo" style="left:88px;top:40px;color:var(--ink)">Belvoro Group</div>
  <p class="abs" style="left:90px;top:127px;width:350px;font-size:13.5px;line-height:24px;color:var(--muted)">Lorem ipsum dolor sit amet consectetur adipiscing eiusmod tempor incididunt ut labore et dolore magna aliqua.</p>
  <nav class="footer-nav">
    <a style="left:828px">Home</a>
    <a style="left:923px">About Us</a>
    <a style="left:1039px">Services</a>
  </nav>
  <div class="abs" style="left:860px;top:126px;font-size:17px;color:var(--ink);display:flex;align-items:center">
    <svg width="14" height="19" viewBox="0 0 14 19" style="margin-right:14px"><path d="M7 0C3.1 0 0 3.1 0 7c0 5 7 12 7 12s7-7 7-12c0-3.9-3.1-7-7-7zm0 9.6A2.6 2.6 0 1 1 7 4.4a2.6 2.6 0 0 1 0 5.2z" fill="#1d1d26"/></svg>
    418 E. Larkfield Ave. #204
  </div>
  <span class="social" style="left:947px" aria-label="Social link"></span>
  <span class="social" style="left:991px" aria-label="Social link"></span>
  <span class="social" style="left:1038px" aria-label="Social link"></span>
  <span class="social" style="left:1089px" aria-label="Social link"></span>
  <div class="abs" style="left:88px;top:227px;width:1026px;height:1px;background:#cfcfd4"></div>
  <p class="abs" style="left:90px;top:244px;font-size:13px;color:var(--ink)">© Belvoro Group. All Rights Reserved.</p>
</footer>

</body>
</html>
```